Bytemill - a software development company requires letter head

I currently have a business card and logo, I just need a nice looking letter head the matches the two. I will upload these Illustrator files.

I would like the letter head to be done in a current version of MS Word.

Please incorporate 'bytemill' as per the attached font and the logo.

Industry/Entity Type

Computer Software

Colors

Designer to choose colors to be used in the design.

Requirements
Must have
• Fits in with current design, sleek and professional. It will be used for quotations and tenders and documentation going to clients and potential clients.
• Would like to company logo up the top header and perhaps a watermark of the logo at the bottom right, a bit like the business card.
• Also it needs to be MS word.
• Please work with the color pallet from the attached files.

```html
<!DOCTYPE html>
<html lang="en">
<head>
<meta charset="utf-8">
<title>Bytemill Letterhead</title>
<link rel="stylesheet" href="https://fonts.googleapis.com/css2?family=Open+Sans:wght@400;600;700&display=swap">
<style>
  :root {
    --backdrop: #e4e4e4;
    --paper: #fafafa;
    --ink: #3a3a3a;
    --ink-strong: #111111;
    --brand-blue: #27a8e0;
    --band: #4a4a4a;
    --band-text: #f2f2f2;
    --signature-tone: #d6d6d6;
  }
  * { box-sizing: border-box; margin: 0; padding: 0; }
  html, body { width: 1200px; height: 945px; overflow: hidden; }
  body {
    background: var(--backdrop);
    font-family: "Open Sans", Arial, sans-serif;
    color: var(--ink);
    position: relative;
  }
  .letterhead {
    position: absolute;
    left: 290px;
    top: 34px;
    width: 620px;
    height: 877px;
    background: var(--paper);
    box-shadow: 0 6px 18px rgba(0,0,0,0.12);
    overflow: hidden;
  }
  .header-brand {
    position: absolute;
    top: 62px;
    right: 70px;
    font-size: 30px;
    font-weight: 600;
    letter-spacing: 2px;
    text-transform: uppercase;
    color: var(--brand-blue);
  }
  .letter-body {
    position: absolute;
    left: 60px;
    top: 250px;
    width: 500px;
    font-size: 12px;
    line-height: 1.32;
  }
  .greeting {
    font-weight: 700;
    font-size: 14px;
    color: var(--ink-strong);
    margin-bottom: 12px;
  }
  .letter-body p.copy { margin-bottom: 14px; }
  .signature {
    position: absolute;
    left: 62px;
    top: 620px;
    width: 130px;
    height: 44px;
    border-radius: 4px;
    background: var(--signature-tone);
  }
  .footer-band {
    position: absolute;
    left: 0;
    bottom: 0;
    width: 620px;
    height: 170px;
  }
  .footer-mark {
    position: absolute;
    right: 28px;
    bottom: 110px;
    display: flex;
    align-items: center;
    gap: 8px;
    font-size: 18px;
    font-weight: 600;
    text-transform: uppercase;
    color: var(--brand-blue);
  }
  .footer-mark .dot {
    width: 14px; height: 14px; border-radius: 50%;
    background: var(--brand-blue);
  }
  .footer-info {
    position: absolute;
    left: 60px;
    bottom: 18px;
    display: flex;
    align-items: center;
    gap: 18px;
    color: var(--band-text);
    font-size: 12px;
  }
  .contact-list { list-style: none; }
  .contact-list li {
    display: flex; align-items: center; gap: 7px;
    line-height: 1.55;
  }
  .contact-list svg { width: 13px; height: 13px; flex: none; }
  .divider { width: 1px; height: 50px; background: #8a8a8a; }
  .company-name {
    color: var(--brand-blue);
    font-weight: 700;
    text-transform: uppercase;
    font-size: 12px;
  }
</style>
</head>
<body>
  <main class="letterhead">
    <div class="header-brand">Bytemill</div>

    <section class="letter-body">
      <p class="greeting">Dear Mr. Carter,</p>
      <p class="copy">Lorem Ipsum is simply dummy text of the printing and typesetting industry. Lorem Ipsum has been the industry's standard dummy text ever since the 1500s, when an unknown printer took a galley of type and scrambled it to make a type specimen book. It has survived not only five centuries, but also the leap into electronic typesetting, remaining essentially unchanged.</p>
      <p class="copy">The standard chunk of Lorem Ipsum used since the 1500s is reproduced below for those interested. Sections 1.10.32 and 1.10.33 from "de Finibus Bonorum et Malorum" by Cicero are also reproduced in their exact original form, accompanied by English versions from the 1914 translation by H. Rackham</p>
      <p class="copy">Lorem Ipsum is simply dummy text of the printing and typesetting industry. Lorem Ipsum has been the industry's standard dummy text ever since the 1500s, when an unknown printer took a galley of type and scrambled it to make a type specimen book. It has survived not only five centuries, but also the leap into electronic typesetting, remaining essentially unchanged. It was popularised in the</p>
      <p class="copy">The standard chunk of Lorem Ipsum used since the 1500s is reproduced below for those interested. Sections 1.10.32 and 1.10.33 from "de Finibus Bonorum et Malorum" by Cicero are also reproduced in their exact original form, accompanied by English versions from the 1914 translation by H. Rackham</p>
    </section>

    <div class="signature" role="img" aria-label="Handwritten signature"></div>

    <svg class="footer-band" viewBox="0 0 620 170" preserveAspectRatio="none" aria-hidden="true">
      <polygon points="0,90 620,20 620,170 0,170" fill="var(--band)"/>
    </svg>

    <div class="footer-mark"><span class="dot"></span>Bytemill</div>

    <footer class="footer-info">
      <ul class="contact-list">
        <li>
          <svg viewBox="0 0 16 16"><circle cx="8" cy="8" r="8" fill="var(--brand-blue)"/><path d="M5.5 4.5l1.5 0 .6 2-1 .8a5 5 0 0 0 2.1 2.1l.8-1 2 .6v1.5c0 .4-.4.8-.8.8A6.2 6.2 0 0 1 4.7 5.3c0-.4.4-.8.8-.8z" fill="#fff"/></svg>
          +61 400 12 3456
        </li>
        <li>
          <svg viewBox="0 0 16 16"><circle cx="8" cy="8" r="8" fill="var(--brand-blue)"/><rect x="4" y="5.2" width="8" height="5.6" rx="0.6" fill="#fff"/><path d="M4.3 5.5L8 8.4l3.7-2.9" stroke="var(--brand-blue)" stroke-width="0.9" fill="none"/></svg>
          hello@bytemill.co
        </li>
        <li>
          <svg viewBox="0 0 16 16"><circle cx="8" cy="8" r="8" fill="var(--brand-blue)"/><circle cx="8" cy="8" r="3.6" fill="none" stroke="#fff" stroke-width="0.9"/><path d="M4.4 8h7.2M8 4.4c-1.6 2-1.6 5.2 0 7.2M8 4.4c1.6 2 1.6 5.2 0 7.2" stroke="#fff" stroke-width="0.8" fill="none"/></svg>
          www.bytemill.co
        </li>
      </ul>
      <span class="divider"></span>
      <address style="font-style: normal;">
        <div class="company-name">Bytemill</div>
        <div>Po Box 218 Harbourview Sa 5090</div>
      </address>
    </footer>
  </main>
</body>
</html>
```